Creative Law Firm Business Card

attached are photos of myself and our office as well as language that I would like to see on the card, likely on the back, although I leave that to the designer. I have also attached copies of both sides of a marketing card that we produced just for ideas. I would like to find a tactful way to get my photo in along with the office. I attached copies of our logo, both normal and inverted.

I listed my name as Glen Whitacre to be casual, however, it should probably read Glenford T Whitacre

Requirements
Must have
• attached file #8 has content.
• I would like my picture and the office photo on page 1
• The text, with the exception of the firm name "WHITACRE & LOMAX" and the firm description underneath it "THE BUSINESS AND BANKRUPTCY LAWYERS", should be on the back. The layout and fonts are up to the designer

```html
<!DOCTYPE html>
<html lang="en">
<head>
<meta charset="utf-8">
<title>Whitacre &amp; Lomax – Business Card</title>
<link rel="stylesheet" href="https://fonts.googleapis.com/css2?family=Cinzel:wght@400;600&display=swap">
<style>
  :root{
    --backdrop:#e4e4e4;
    --navy:#1c2a5c;
    --sky:#2f5fb8;
    --sky-light:#7fa6e0;
    --stone:#d9c7a8;
    --accent-blue:#6f9fdc;
    --white:#ffffff;
    --paper:#fbfbfb;
  }
  *{box-sizing:border-box;margin:0;padding:0}
  html,body{width:1200px;height:852px;overflow:hidden;background:var(--backdrop)}
  body{position:relative;font-family:"Cinzel",serif}

  .card{position:absolute;top:271px;width:540px;height:310px;border-radius:18px;overflow:hidden;box-shadow:0 3px 10px rgba(0,0,0,.18)}
  .card--front{left:40px}
  .card--back{left:620px;background:var(--paper)}

  /* Front */
  .office-photo{position:absolute;inset:0;background:linear-gradient(160deg,var(--sky) 0%,var(--sky-light) 38%,var(--stone) 62%,#8a7a5c 82%,#4b5a3a 100%)}
  .front-heading{position:absolute;left:36px;top:92px;color:var(--white);text-shadow:0 1px 3px rgba(0,0,0,.35)}
  .front-heading .firm-name{font-size:34px;font-weight:400;letter-spacing:1px}
  .front-heading .firm-tagline{font-size:13.5px;letter-spacing:1px;margin-top:4px}

  /* Back */
  .back-shapes{position:absolute;inset:0}
  .portrait{position:absolute;right:18px;top:36px;width:168px;height:196px;border-radius:6px;background:linear-gradient(180deg,#cfd6e2 0%,#9aa3b3 45%,#2a2e38 100%)}
  .brand{position:absolute;left:22px;top:30px;display:flex;align-items:flex-end;gap:10px}
  .brand-square{width:34px;height:34px;background:var(--navy);flex:none}
  .brand-name{font-size:21px;font-weight:600;color:var(--navy);border-top:1.5px solid var(--navy);padding-top:5px;line-height:1;white-space:nowrap}
  .attorney{position:absolute;left:22px;top:84px;width:300px;color:var(--navy)}
  .attorney-name{font-size:17px;font-weight:400}
  .attorney-line{font-size:10.5px;margin-top:3px;white-space:nowrap}
  .motto{font-size:10.5px;margin-top:12px}

  .contacts{position:absolute;left:22px;top:222px;list-style:none;color:var(--white);font-size:9.5px}
  .contacts li{display:flex;align-items:center;gap:8px;height:13px}
  .contacts svg{width:9px;height:9px;fill:var(--white)}
  .practice{position:absolute;left:22px;bottom:10px;color:var(--white);font-size:15px;letter-spacing:.5px}
</style>
</head>
<body>

<section class="card card--front">
  <div class="office-photo" role="img" aria-label="Photo of the firm's office building framed by palm trees under a blue sky"></div>
  <div class="front-heading">
    <h1 class="firm-name">WHITACRE &amp; LOMAX</h1>
    <p class="firm-tagline">THE BUSINESS &amp; BANKRUPTCY LAWYERS</p>
  </div>
</section>

<section class="card card--back">
  <svg class="back-shapes" viewBox="0 0 540 310" preserveAspectRatio="none" aria-hidden="true">
    <path d="M0 212 C140 200 300 185 540 158 L540 310 L0 310 Z" fill="var(--navy)"/>
    <path d="M0 206 C140 194 300 179 540 150 L540 156 C300 184 140 200 0 210 Z" fill="var(--accent-blue)"/>
  </svg>
  <div class="portrait" role="img" aria-label="Portrait photo of attorney Glenford T Whitacre in a dark suit"></div>

  <div class="brand">
    <span class="brand-square"></span>
    <h2 class="brand-name">WHITACRE &amp; LOMAX</h2>
  </div>

  <div class="attorney">
    <p class="attorney-name">Glenford T Whitacre</p>
    <p class="attorney-line">Bankruptcy Specialist - Court Appointed Mediator</p>
    <p class="attorney-line">Over 35 Years Experience - AV Rated</p>
    <p class="motto">We Find an Exit Strategy Before We Act</p>
  </div>

  <ul class="contacts">
    <li><svg viewBox="0 0 10 10"><path d="M2 0.5 L3.6 2.6 L2.8 3.6 C3.4 5 4.9 6.5 6.4 7.2 L7.4 6.4 L9.5 8 L8.3 9.5 C4.5 9 1 5.5 0.5 1.7 Z"/></svg>714-555-0182</li>
    <li><svg viewBox="0 0 10 10"><path d="M0.5 2 H9.5 V8 H0.5 Z M1 2.4 L5 5.4 L9 2.4"/></svg>glen@whitacrelomax.com</li>
    <li><svg viewBox="0 0 10 10"><circle cx="5" cy="5" r="4.5"/></svg>www.whitacrelomax.com</li>
    <li><svg viewBox="0 0 10 10"><path d="M5 0.5 C7.3 0.5 8.5 2.2 8.5 4 C8.5 6.2 5 9.5 5 9.5 C5 9.5 1.5 6.2 1.5 4 C1.5 2.2 2.7 0.5 5 0.5 Z"/></svg>1200 Harbor View Dr Irvine CA 92618</li>
  </ul>
  <p class="practice">Commercial Law &amp; Litigation</p>
</section>

</body>
</html>
```